Business card design needed

Hi,
I was hoping to have a business card designed with a background similar to dark coloured concrete texture. I have a photo of the particular concrete that I would like to be used as the background but for some reason it wouldn't let me upload the image. Please email me for the image and I will send to you asap.
I would like the company name to be in a font that is thin, crisp to reflect 'precision'. I am trying to convey that my services are more precise and have more attention to detail than my competitors. I would like this to be represented through the font if possible.
Colours are at your discretion - although we would like it to attract the eye and stand out. We would like the card to be in a modern style.
I was thinking for an image in the background of the card, or on the side of the card wherever is appropriate, half of a ring saw blade or similar.
The company is a concrete cutting and drilling service - we are a 24 hour 7 day service which is unique to the industry. We provide a more detailed service to our customers and this is the backbone of our reputation.
Target Market(s)
Construction industry & general public
Industry/Entity Type
Concrete
Contact Information for Business Card
Ridgeline Saw & Bore Pty Ltd
Concrete Cutting & Drilling
24 hour 7 day service
Trevor Halloway
Director
M: 0412 908 251
P: (07) 3196 4027
E: ridgelinesawandbore@mailbrook.example
PO Box 318, Wendaroo DC QLD 4172

```html
<!DOCTYPE html>
<html lang="en">
<head>
<meta charset="utf-8">
<title>Ridgeline Saw &amp; Bore – Business Card</title>
<link rel="stylesheet" href="https://fonts.googleapis.com/css2?family=Roboto+Condensed:wght@700&family=Open+Sans:ital,wght@0,400;0,600;0,700;1,700&display=swap">
<style>
  :root {
    --red: #e31e24;
    --ink: #222222;
    --white: #ffffff;
    --concrete-light: #d9dcdf;
    --concrete-mid: #a9adb2;
    --concrete-dark: #6f7378;
    --band-light: rgba(235, 237, 239, 0.75);
    --band-dark: rgba(58, 60, 63, 0.88);
    --panel: rgba(236, 238, 240, 0.72);
    --rule: #6b6e72;
    --blade: #9a9bb8;
  }
  * { margin: 0; padding: 0; box-sizing: border-box; }
  html, body {
    width: 1120px; height: 1200px; overflow: hidden;
    background: var(--white);
    font-family: "Open Sans", Arial, sans-serif;
  }
  .card { position: absolute; overflow: hidden; }
  .card--front { left: 130px; top: 110px; width: 837px; height: 480px; }
  .card--back  { left: 125px; top: 637px; width: 834px; height: 478px; }

  .concrete {
    position: absolute; inset: 0;
    background:
      radial-gradient(ellipse at 30% 40%, var(--concrete-light) 0%, transparent 60%),
      radial-gradient(ellipse at 80% 70%, var(--concrete-light) 0%, transparent 55%),
      linear-gradient(160deg, var(--concrete-mid) 0%, var(--concrete-light) 45%, var(--concrete-mid) 75%, var(--concrete-dark) 100%);
  }

  /* front */
  .band-light {
    position: absolute; left: 0; top: 52px; width: 837px; height: 128px;
    background: var(--band-light);
  }
  .band-dark {
    position: absolute; left: 0; top: 182px; width: 552px; height: 212px;
    background: var(--band-dark);
  }
  .company {
    position: absolute; left: 73px; top: 58px;
    font-family: "Roboto Condensed", "Arial Narrow", sans-serif;
    font-weight: 700; font-size: 36px; color: var(--red);
    text-transform: uppercase; letter-spacing: 0.2px; white-space: nowrap;
  }
  .company .suffix { font-size: 22px; text-transform: none; }
  .service-line {
    position: absolute; left: 73px; top: 104px;
    font-size: 27px; font-weight: 600; color: var(--ink);
  }
  .abn {
    position: absolute; left: 73px; top: 146px;
    font-size: 20px; font-weight: 700; color: var(--ink);
  }
  .person { position: absolute; left: 73px; top: 206px; color: var(--white); }
  .person__name { font-size: 24px; color: var(--red); font-weight: 400; line-height: 32px; }
  .person__role { font-size: 24px; line-height: 38px; }
  .contact { list-style: none; margin-top: 12px; }
  .contact li { font-size: 20px; font-weight: 700; line-height: 33px; white-space: nowrap; }
  .postal {
    position: absolute; left: 73px; top: 395px;
    font-size: 19px; color: var(--white);
  }

  .blade {
    position: absolute; left: 511px; top: 76px; width: 326px; height: 326px;
    border-radius: 50%;
    border: 26px solid var(--blade);
    background: radial-gradient(circle, rgba(255,255,255,0.25) 0%, rgba(200,202,210,0.15) 70%);
  }
  .round-clock {
    position: absolute; left: 630px; top: 206px; width: 170px;
    text-align: center; color: var(--red); font-weight: 700;
  }
  .round-clock__hours { display: block; font-size: 44px; line-height: 48px; }
  .round-clock__label { display: block; font-size: 20px; line-height: 26px; }

  /* back */
  .quote-panel {
    position: absolute; left: 62px; top: 45px; width: 703px; height: 377px;
    background: var(--panel);
  }
  .quote-title {
    position: absolute; left: 0; right: 0; top: 8px;
    text-align: center; font-size: 36px; font-weight: 600; color: var(--red);
  }
  .quote-line {
    position: absolute; left: 102px; width: 631px; height: 2px; background: var(--rule);
  }
  .tagline {
    position: absolute; left: 0; right: 0; top: 378px;
    text-align: center; font-size: 25px; font-weight: 700; font-style: italic; color: var(--red);
  }
</style>
</head>
<body>

<section class="card card--front">
  <div class="concrete" role="img" aria-label="Dark concrete texture background"></div>
  <div class="band-light"></div>
  <div class="band-dark"></div>

  <div class="blade" role="img" aria-label="Ring saw blade illustration"></div>
  <p class="round-clock">
    <span class="round-clock__hours">24/7</span>
    <span class="round-clock__label">service</span>
  </p>

  <h1 class="company">Ridgeline Saw &amp; Bore <span class="suffix">Pty Ltd</span></h1>
  <p class="service-line">concrete cutting &amp; drilling</p>
  <p class="abn">ABN: 52 781 306 194</p>

  <div class="person">
    <p class="person__name">Trevor Halloway</p>
    <p class="person__role">Director</p>
    <ul class="contact">
      <li>M. 0412 908 251</li>
      <li>Ph. (07) 3196 4027</li>
      <li>ridgelinesawandbore@mailbrook.example</li>
    </ul>
  </div>
  <p class="postal">PO Box 318, Wendaroo DC QLD 4172</p>
</section>

<section class="card card--back">
  <div class="concrete" role="img" aria-label="Dark concrete texture background"></div>
  <div class="quote-panel">
    <h2 class="quote-title">Quote</h2>
  </div>
  <div class="quote-line" style="top:179px"></div>
  <div class="quote-line" style="top:240px"></div>
  <div class="quote-line" style="top:302px"></div>
  <p class="tagline">When near enough isn't good enough</p>
</section>

</body>
</html>
```